Business Card Design needed for start up company Pelmora

In need of a new business card designed for a start up company based in Sydney, Pelmora is a new start up innovative Company, our mission it to make property accessible for everyday Australian and to become the leading Real Estate platform in Australia. We want it to be fresh and clean.

Industry/Entity Type

Financial

Contact Information for Business Card

Section for Name
Section for Title

PELMORA - Keys Within Reach
Mobile:
Direct:

Font styles to use
Sans Serif

Colors
33a6d7
0692cd
0255a3
ffffff

Requirements
Must have
• Logo, all business card details

```html
<!DOCTYPE html>
<html lang="en">
<head>
<meta charset="utf-8">
<title>Pelmora Business Card</title>
<link href="https://fonts.googleapis.com/css2?family=Open+Sans:wght@400;600&display=swap" rel="stylesheet">
<style>
  :root {
    --bg: #e9e7e5;
    --card: #1b1b1d;
    --card-pattern-a: #232326;
    --card-pattern-b: #1d1d20;
    --sky: #33a6d7;
    --azure: #0692cd;
    --navy: #0255a3;
    --white: #ffffff;
    --grey: #a9a9ad;
    --rule: #8d8d92;
  }
  * { margin: 0; padding: 0; box-sizing: border-box; }
  html, body {
    width: 1200px; height: 864px; overflow: hidden;
    background: var(--bg);
    font-family: "Open Sans", sans-serif;
  }
  .canvas { position: relative; width: 1200px; height: 864px; }
  .card {
    position: absolute;
    width: 540px; height: 309px;
    background: var(--card);
    border-radius: 4px;
    box-shadow: 0 10px 26px rgba(0,0,0,0.28);
    overflow: hidden;
  }
  .card-front { left: 40px; top: 170px; }
  .card-back { left: 620px; top: 385px; }

  .brand-pattern {
    position: absolute; inset: 0;
    background: linear-gradient(135deg, var(--card-pattern-a), var(--card-pattern-b));
  }
  .front-brand {
    position: absolute; left: 180px; top: 152px;
    font-weight: 600; font-size: 34px; letter-spacing: 4px;
    line-height: 1; color: var(--grey);
  }
  .tagline {
    position: absolute; left: 181px; top: 200px;
    font-size: 14px; color: var(--grey);
  }

  .back-brand {
    position: absolute; right: 30px; top: 62px;
    font-weight: 600; font-size: 34px; letter-spacing: 4px;
    line-height: 1; color: var(--white);
  }
  .person { position: absolute; left: 34px; top: 56px; }
  .person .name {
    font-weight: 600; font-size: 15px; letter-spacing: 0.5px;
    color: var(--azure); text-transform: uppercase;
  }
  .person .title {
    font-size: 14px; color: var(--sky); text-transform: uppercase;
    margin-top: 2px;
  }
  .contacts {
    position: absolute; left: 34px; top: 112px;
    list-style: none; font-size: 13.5px; color: var(--white);
  }
  .contacts li { display: flex; align-items: center; gap: 10px; line-height: 22px; }
  .contacts svg { width: 12px; height: 12px; fill: var(--azure); flex: none; }
  .divider {
    position: absolute; left: 34px; right: 30px; top: 184px;
    height: 1px; background: var(--rule);
  }
  .address {
    position: absolute; right: 30px; top: 216px;
    text-align: right; font-size: 14px; line-height: 21px; color: var(--white);
    font-style: normal;
  }
</style>
</head>
<body>
<div class="canvas">

  <section class="card card-front">
    <div class="brand-pattern" role="img" aria-label="Faint repeating brand name pattern across the card background"></div>
    <p class="front-brand">PELMORA</p>
    <p class="tagline">Keys Within Reach</p>
  </section>

  <section class="card card-back">
    <p class="back-brand">PELMORA</p>
    <div class="person">
      <p class="name">Liam Hartley</p>
      <p class="title">CEO/Founder</p>
    </div>
    <ul class="contacts">
      <li>
        <svg viewBox="0 0 12 12" aria-hidden="true"><path d="M1 4c0-2 1-3 5-3s5 1 5 3l-2 1-1-1H4L3 5zM2 6h8l1 5H1z"/></svg>
        0412 555 208
      </li>
      <li>
        <svg viewBox="0 0 12 12" aria-hidden="true"><path d="M3 0h6a1 1 0 0 1 1 1v10a1 1 0 0 1-1 1H3a1 1 0 0 1-1-1V1a1 1 0 0 1 1-1zm0 2v8h6V2z"/></svg>
        02 5550 1374
      </li>
      <li>
        <svg viewBox="0 0 12 12" aria-hidden="true"><path d="M0 2h12v8H0z"/></svg>
        liam@pelmora.com.au
      </li>
    </ul>
    <div class="divider"></div>
    <address class="address">
      48 Harbour Row<br>
      Sydney, NSW 2000<br>
      www.pelmora.com.au
    </address>
  </section>

</div>
</body>
</html>
```